Thank you for shopping with us business card

We would like a thank you card for our rebranded business. We used to be "Brindle Goods" but are now "Marlow Finds. Old thank you card and new logo will be attached for reference. New thank you card does not have to be same design as old thank you card, but please use new logo.
Shopmart URL is now marlowfinds.shopmart.example
Instagram is @Marlow_Finds
Email is marlowfinds@mailbox.example
Thank you!

Contact Information for Business Card

Shopmart site, email, Instagram

```html
<!DOCTYPE html>
<html lang="en">
<head>
<meta charset="utf-8">
<title>Marlow Finds – Thank You Card</title>
<link rel="stylesheet" href="https://fonts.googleapis.com/css2?family=Montserrat:wght@500;700&family=Raleway:wght@500&family=Mr+Dafoe&family=Lobster+Two:ital,wght@1,700&display=swap">
<style>
  :root {
    --stage: #000000;
    --card-green: #bdf9bd;
    --card-green-soft: #c8fbc6;
    --brand-orange: #e0622e;
    --deep-orange: #c9420f;
    --edge-tint: rgba(224, 98, 46, 0.28);
    --edge-clear: rgba(224, 98, 46, 0);
  }
  * { margin: 0; padding: 0; box-sizing: border-box; }
  html, body {
    width: 975px; height: 1200px; overflow: hidden;
    background: var(--stage);
  }
  .sheet { position: relative; width: 975px; height: 1200px; }
  .card {
    position: absolute; left: 88px; width: 798px; height: 532px;
    overflow: hidden;
    background: radial-gradient(ellipse at 40% 30%, var(--card-green-soft), var(--card-green) 70%);
  }
  .card--front { top: 61px; }
  .card--back { top: 608px; }

  .edge-ornament {
    position: absolute; top: 0; height: 532px;
  }
  .edge-ornament--left {
    left: 0; width: 150px;
    background: linear-gradient(to right, var(--edge-tint), var(--edge-clear));
  }
  .edge-ornament--right {
    right: 0; width: 150px;
    background: linear-gradient(to left, var(--edge-tint), var(--edge-clear));
  }
  .card--back .edge-ornament--left,
  .card--back .edge-ornament--right { width: 110px; }

  .brand-mark {
    position: absolute; left: 344px; top: 100px;
    width: 110px; height: 110px;
    background: var(--brand-orange);
  }
  .brand-name {
    position: absolute; left: 0; right: 0; top: 299px;
    text-align: center;
    font: 500 23px/1 "Montserrat", sans-serif;
    color: var(--brand-orange);
    text-transform: uppercase;
  }
  .contact-list {
    position: absolute; left: 0; right: 0; top: 347px;
    list-style: none; text-align: center;
    font: 700 18px/32.5px "Montserrat", sans-serif;
    color: var(--brand-orange);
  }

  .thanks-title {
    position: absolute; left: 0; right: 0; top: 70px;
    text-align: center;
    font: 400 150px/1 "Mr Dafoe", cursive;
    color: var(--deep-orange);
    white-space: nowrap;
  }
  .thanks-divider {
    position: absolute; left: 203px; top: 240px; width: 405px; height: 60px;
  }
  .thanks-sub {
    position: absolute; left: 0; right: 0; top: 305px;
    text-align: center;
    font: italic 700 46px/1 "Lobster Two", cursive;
    color: var(--deep-orange);
  }
  .thanks-note {
    position: absolute; left: 0; right: 0; top: 384px;
    text-align: center;
    font: 500 20px/33px "Raleway", sans-serif;
    color: var(--brand-orange);
  }
</style>
</head>
<body>
<main class="sheet">

  <section class="card card--front" aria-label="Business card front">
    <div class="edge-ornament edge-ornament--left" role="img" aria-label="Column of orange starburst ornaments"></div>
    <div class="edge-ornament edge-ornament--right" role="img" aria-label="Column of orange starburst ornaments"></div>

    <div class="brand-mark" aria-hidden="true"></div>
    <h1 class="brand-name">Marlow Finds</h1>
    <ul class="contact-list">
      <li>Email: marlowfinds@mailbox.example</li>
      <li>Website: marlowfinds.shopmart.example</li>
      <li>Instagram: @Marlow_Finds</li>
    </ul>
  </section>

  <section class="card card--back" aria-label="Business card back">
    <div class="edge-ornament edge-ornament--left" role="img" aria-label="Orange starburst ornaments along the left edge"></div>
    <div class="edge-ornament edge-ornament--right" role="img" aria-label="Orange starburst ornaments along the right edge"></div>

    <h2 class="thanks-title">Thank You</h2>
    <svg class="thanks-divider" viewBox="0 0 405 60" aria-hidden="true">
      <g stroke="#c9420f" stroke-width="6" stroke-dasharray="22 6" fill="none">
        <line x1="0" y1="28" x2="158" y2="28"/>
        <line x1="250" y1="28" x2="405" y2="28"/>
      </g>
      <ellipse cx="203" cy="22" rx="9" ry="24" fill="none" stroke="#c9420f" stroke-width="4" transform="rotate(15 203 22)"/>
    </svg>
    <p class="thanks-sub">for your purchase</p>
    <p class="thanks-note">Your purchase made my day and I hope this package brightens yours.<br>please come back and leave a review!</p>
  </section>

</main>
</body>
</html>
```